Veltora Software Business Card Design

We are a new organization called Veltora. We are a software as a service provider. We deliver a project and program management solution via the internet, so everyone has the ability to work together and collaborate. Its an enterprise platform and we will focus on 50 plus employee company.

We have a website in place
www.veltora-demo.com

Use this as a start of producing the business card. The logo is there as well, but if you have a great and better solution...

Color scheme's could be inline with the website, but don't pin point on it. We can always change the website, logo, color scheme etc.

Target Market(s)

B2B, Projectmembers, projectmanagers, ICT, CTO, Marketing Managers

Industry/Entity Type

Software

Requirements
Must have
• Marten Kuyvelsma

Tel: +31 255 47 09 36
Mob: +31 6 927 15 062
marten@veltora-demo.com
Oostelingpad 84c
2184 KT Haverdijk

Www.veltora-demo.com
social media links

```html
<!DOCTYPE html>
<html lang="en">
<head>
<meta charset="utf-8">
<title>Veltora Business Card</title>
<link rel="stylesheet" href="https://fonts.googleapis.com/css2?family=Montserrat:wght@300;400&display=swap">
<style>
  :root {
    --lime: #bcc527;
    --ink: #3b3b3b;
    --paper: #f7f7f5;
    --backdrop: #d9d9d7;
    --icon-dark: #3a3a3a;
    --white: #ffffff;
  }
  * { margin: 0; padding: 0; box-sizing: border-box; }
  html, body {
    width: 1200px;
    height: 900px;
    overflow: hidden;
    background: var(--backdrop);
    font-family: "Montserrat", Arial, sans-serif;
  }
  .canvas {
    position: relative;
    width: 1200px;
    height: 900px;
    display: flex;
    flex-direction: column;
    align-items: center;
    justify-content: center;
    gap: 40px;
  }
  .card {
    position: relative;
    width: 640px;
    height: 390px;
    box-shadow: 0 6px 18px rgba(0, 0, 0, 0.18);
    overflow: hidden;
  }

  /* Front */
  .card-front {
    background: var(--lime);
    display: flex;
    flex-direction: column;
    align-items: center;
    justify-content: center;
  }
  .front-wordmark {
    color: var(--white);
    font-weight: 300;
    font-size: 112px;
    letter-spacing: 1px;
    line-height: 1;
    margin-top: -10px;
  }
  .social-links {
    display: flex;
    gap: 22px;
    margin-top: 46px;
  }
  .social-dot {
    width: 30px;
    height: 30px;
    border-radius: 50%;
    background: var(--icon-dark);
  }

  /* Back */
  .card-back {
    background: var(--paper);
    color: var(--ink);
    padding: 38px 48px;
  }
  .back-wordmark {
    color: var(--lime);
    font-weight: 300;
    font-size: 64px;
    line-height: 1;
    letter-spacing: 0.5px;
  }
  .holder-name {
    margin-top: 50px;
    font-weight: 400;
    font-size: 26px;
    letter-spacing: 0.6px;
    white-space: nowrap;
  }
  .contact-columns {
    display: flex;
    justify-content: space-between;
    margin-top: 16px;
  }
  .contact-list {
    list-style: none;
    display: flex;
    flex-direction: column;
    flex: none;
    gap: 8px;
  }
  .contact-list--right { margin-top: 32px; }
  .contact-item {
    display: flex;
    align-items: flex-start;
    gap: 12px;
    font-size: 16px;
    font-weight: 400;
    letter-spacing: 0.4px;
    line-height: 24px;
    white-space: nowrap;
  }
  .contact-icon {
    flex: none;
    width: 24px;
    height: 24px;
  }
</style>
</head>
<body>
<main class="canvas">

  <section class="card card-front" aria-label="Business card front">
    <div class="front-wordmark">Veltora</div>
    <div class="social-links" aria-label="Social media links">
      <span class="social-dot"></span>
      <span class="social-dot"></span>
    </div>
  </section>

  <section class="card card-back" aria-label="Business card back">
    <div class="back-wordmark">Veltora</div>
    <div class="holder-name">Marten Kuyvelsma</div>

    <div class="contact-columns">
      <ul class="contact-list">
        <li class="contact-item">
          <svg class="contact-icon" viewBox="0 0 24 24" aria-hidden="true">
            <circle cx="12" cy="12" r="12" fill="var(--lime)"/>
            <path d="M8 6.5c.6-.4 1.2-.3 1.5.2l1.2 2c.3.5.2 1-.3 1.3l-.7.5c.6 1.6 1.6 2.8 3.1 3.7l.6-.6c.4-.4 1-.4 1.4 0l1.7 1.5c.4.4.4 1-.1 1.4l-.9.8c-3.6-.4-7.3-4.6-7.6-8.9z" fill="var(--white)"/>
          </svg>
          <span>+31 255 47 09 36</span>
        </li>
        <li class="contact-item">
          <svg class="contact-icon" viewBox="0 0 24 24" aria-hidden="true">
            <circle cx="12" cy="12" r="12" fill="var(--lime)"/>
            <rect x="8.5" y="5.5" width="7" height="13" rx="1.2" fill="none" stroke="var(--white)" stroke-width="1.5"/>
            <circle cx="12" cy="16" r="0.9" fill="var(--white)"/>
          </svg>
          <span>+31 6 927 15 062</span>
        </li>
        <li class="contact-item">
          <svg class="contact-icon" viewBox="0 0 24 24" aria-hidden="true">
            <circle cx="12" cy="12" r="12" fill="var(--lime)"/>
            <rect x="6" y="8" width="12" height="8.5" rx="0.8" fill="none" stroke="var(--white)" stroke-width="1.4"/>
            <path d="M6.3 8.4 12 13l5.7-4.6" fill="none" stroke="var(--white)" stroke-width="1.4"/>
          </svg>
          <span>marten@veltora-demo.com</span>
        </li>
      </ul>

      <ul class="contact-list contact-list--right">
        <li class="contact-item">
          <svg class="contact-icon" viewBox="0 0 24 24" aria-hidden="true">
            <circle cx="12" cy="12" r="12" fill="var(--lime)"/>
            <rect x="8.5" y="6.5" width="7" height="11" rx="3.5" fill="none" stroke="var(--white)" stroke-width="1.4"/>
            <line x1="12" y1="6.8" x2="12" y2="10.5" stroke="var(--white)" stroke-width="1.4"/>
            <line x1="8.8" y1="10.5" x2="15.2" y2="10.5" stroke="var(--white)" stroke-width="1.4"/>
          </svg>
          <span>www.veltora-demo.com</span>
        </li>
        <li class="contact-item">
          <svg class="contact-icon" viewBox="0 0 24 24" aria-hidden="true">
            <circle cx="12" cy="12" r="12" fill="var(--lime)"/>
            <path d="M12 5.5a4.5 4.5 0 0 0-4.5 4.5c0 3.3 4.5 8.5 4.5 8.5s4.5-5.2 4.5-8.5A4.5 4.5 0 0 0 12 5.5z" fill="none" stroke="var(--white)" stroke-width="1.4"/>
            <circle cx="12" cy="10" r="1.6" fill="var(--white)"/>
          </svg>
          <span>Oostelingpad 84c<br>2184 KT Haverdijk</span>
        </li>
      </ul>
    </div>
  </section>

</main>
</body>
</html>
```